UI/ UX Design for ERP Software

We need a new UX/UI interface for a ERP software for property managers. Our CMMS / ERP solution is made based on responsive design technologies and is coded in PHP.
The overall UX to be similar to Zel Kavo - easy navigation, intuitive menus.

Industry/Entity Type

Property Management

Number of Pages Required

5+ page

Requirements
Must have
• Round dock buttons
Consistent icons across the application
Enough Spacing between buttons/icons/ menu
Consistent Font
Nice to have
• We would like the UX to allow the users to use the application without /minimum training.
Should not have
• we don't want anything that is classic with respect to UX

```html
<!DOCTYPE html>
<html lang="en">
<head>
<meta charset="utf-8">
<title>Estavo — Property ERP Dashboard</title>
<link href="https://fonts.googleapis.com/css2?family=Roboto:wght@400;500&display=swap" rel="stylesheet">
<style>
  :root{
    --page:#ffffff;
    --shell:#f4f4f4;
    --panel:#ffffff;
    --line:#e6e6e6;
    --grid:#ececec;
    --text:#3a3a3a;
    --muted:#8a8a8a;
    --icon:#b9b9b9;
    --brand:#0a8dff;
    --card-a:#00b6ff;
    --card-b:#0a6af3;
    --alert:#e62828;
    --online:#2bc94a;
  }
  *{box-sizing:border-box;margin:0;padding:0}
  html,body{width:946px;height:1200px;overflow:hidden;background:var(--page);font-family:"Roboto",sans-serif;color:var(--text)}
  .canvas{position:relative;width:946px;height:1200px;overflow:hidden;background:var(--page)}
  .app{position:absolute;left:25px;top:232px;width:896px;height:735px;background:var(--shell);box-shadow:0 6px 24px rgba(0,0,0,.12);overflow:hidden}

  /* top bar */
  .brand{position:absolute;left:0;top:0;width:180px;height:65px;background:var(--panel);border-radius:0 40px 40px 0;display:flex;align-items:center;justify-content:center;gap:8px}
  .brand-mark{width:14px;height:14px;background:var(--brand)}
  .brand-name{font-size:25px;font-weight:500;color:var(--brand)}
  .crumb{position:absolute;left:203px;top:18px;width:86px;text-align:center;font-size:11px;color:var(--muted)}
  .crumb svg{display:block;margin:0 auto 3px}
  .search{position:absolute;left:327px;top:18px;width:314px;height:29px;background:var(--panel);border:1px solid var(--line);font-size:11px;color:var(--muted);padding:8px 11px}
  .search svg{position:absolute;right:9px;top:9px}
  .tool{position:absolute;top:25px}
  .tool .dot{position:absolute;right:-3px;top:-4px;width:6px;height:6px;border-radius:50%;background:var(--alert)}
  .avatar{position:absolute;left:768px;top:16px;width:32px;height:32px;border-radius:50%;background:linear-gradient(135deg,#c89a78,#6b4a3a)}
  .avatar .status{position:absolute;right:-1px;bottom:-1px;width:9px;height:9px;border-radius:50%;background:var(--online);border:2px solid var(--shell)}
  .user{position:absolute;left:812px;top:25px;font-size:11px;color:var(--text)}

  /* sidebar */
  .sidebar{position:absolute;left:0;top:65px;width:182px;height:670px;background:var(--panel);padding-top:16px;list-style:none}
  .nav-item{display:flex;align-items:center;height:28px;padding-left:13px;font-size:11px;color:var(--text)}
  .nav-item svg{width:10px;height:10px;margin-right:13px;fill:var(--icon)}

  /* stat cards */
  .stat{position:absolute;top:71px;width:134px;height:102px;background:linear-gradient(135deg,var(--card-a),var(--card-b));color:#fff;padding:10px 10px}
  .stat svg{display:block;width:14px;height:14px;fill:#fff}
  .stat-value{font-size:17px;font-weight:500;margin-top:7px;white-space:nowrap}
  .stat-value small{font-size:6px;font-weight:400}
  .stat-label{position:absolute;left:10px;bottom:8px;font-size:11px}

  /* range filter */
  .range{position:absolute;left:187px;top:178px;width:693px;height:27px;background:#ececec;font-size:8px;color:var(--muted);text-align:right;padding:8px 10px}
  .range .on{color:var(--brand)}
  .range .sep{margin:0 5px}

  /* chart */
  .chart{position:absolute;left:187px;top:205px;width:693px;height:363px;background:var(--panel);border:1px solid var(--line)}
  .chart svg{display:block}
  .chart text{font-family:"Roboto",sans-serif}
</style>
</head>
<body>
<div class="canvas">
  <main class="app">

    <div class="brand"><span class="brand-mark"></span><span class="brand-name">Estavo</span></div>

    <div class="crumb">
      <svg width="9" height="8" viewBox="0 0 10 9"><path d="M5 0 10 5H8.5V9H6V6H4V9H1.5V5H0Z" fill="#8a8a8a"/></svg>
      Active Dashboard
    </div>

    <div class="search">Search
      <svg width="10" height="10" viewBox="0 0 10 10"><circle cx="4" cy="4" r="3" fill="none" stroke="#8a8a8a" stroke-width="1.3"/><path d="M6.3 6.3 9.5 9.5" stroke="#8a8a8a" stroke-width="1.4"/></svg>
    </div>

    <div class="tool" style="left:678px"><svg width="11" height="11" viewBox="0 0 11 11"><path d="M5.5 1C3.5 1 2.5 2.5 2.5 4.5V7L1 8.5H10L8.5 7V4.5C8.5 2.5 7.5 1 5.5 1ZM4.3 9.3A1.3 1.3 0 0 0 6.7 9.3Z" fill="#8a8a8a"/></svg><span class="dot"></span></div>
    <div class="tool" style="left:703px"><svg width="12" height="10" viewBox="0 0 12 10"><rect x=".6" y=".6" width="10.8" height="8.8" fill="none" stroke="#8a8a8a" stroke-width="1.1"/><path d="M.6 .8 6 5.5 11.4 .8" fill="none" stroke="#8a8a8a" stroke-width="1.1"/></svg><span class="dot"></span></div>
    <div class="tool" style="left:729px"><svg width="11" height="10" viewBox="0 0 11 10"><g fill="#8a8a8a"><rect x="0" y="0" width="2.5" height="2.5"/><rect x="3.5" y="0" width="7.5" height="2.5"/><rect x="0" y="3.7" width="2.5" height="2.5"/><rect x="3.5" y="3.7" width="7.5" height="2.5"/><rect x="0" y="7.4" width="2.5" height="2.5"/><rect x="3.5" y="7.4" width="7.5" height="2.5"/></g></svg></div>

    <div class="avatar" role="img" aria-label="User profile photo"><span class="status"></span></div>
    <div class="user">Marlowe &#8964;</div>

    <ul class="sidebar">
      <li class="nav-item"><svg viewBox="0 0 10 10"><path d="M5 0 10 5H8.5V10H1.5V5H0Z"/></svg>Dashboard</li>
      <li class="nav-item"><svg viewBox="0 0 10 10"><circle cx="3" cy="3" r="2"/><circle cx="7" cy="3" r="2"/><rect x="0" y="6" width="10" height="4" rx="2"/></svg>Customers</li>
      <li class="nav-item"><svg viewBox="0 0 10 10"><rect x="1.5" y="0" width="7" height="10"/></svg>Properties</li>
      <li class="nav-item"><svg viewBox="0 0 10 10"><circle cx="5" cy="3" r="2.5"/><rect x="1" y="6" width="8" height="4" rx="2"/></svg>Tenants</li>
      <li class="nav-item"><svg viewBox="0 0 10 10"><path d="M1 1 3.5 0.5 4.5 3 3 4A6 6 0 0 0 6 7L7 5.5 9.5 6.5 9 9C4 9 1 6 1 1Z"/></svg>Contacts</li>
      <li class="nav-item"><svg viewBox="0 0 10 10"><circle cx="3.5" cy="6" r="3"/><circle cx="8" cy="2.5" r="2"/></svg>Contractors</li>
      <li class="nav-item"><svg viewBox="0 0 10 10"><circle cx="3" cy="3" r="2"/><circle cx="7" cy="3" r="2"/><rect x="0" y="6" width="10" height="4" rx="2"/></svg>Employees</li>
      <li class="nav-item"><svg viewBox="0 0 10 10"><path d="M1.5 0H6.5L8.5 2V10H1.5Z"/></svg>Compliance Managment</li>
      <li class="nav-item"><svg viewBox="0 0 10 10"><circle cx="3.5" cy="6" r="3"/><circle cx="8" cy="2.5" r="2"/></svg>Prevent.Maintenance</li>
      <li class="nav-item"><svg viewBox="0 0 10 10"><circle cx="5" cy="5" r="4.5"/></svg>Work Orders</li>
      <li class="nav-item"><svg viewBox="0 0 10 10"><path d="M3 2 0 5 3 8 4 7 2 5 4 3ZM7 2 10 5 7 8 6 7 8 5 6 3Z"/></svg>Purchase Orders</li>
      <li class="nav-item"><svg viewBox="0 0 10 10"><circle cx="4" cy="4" r="3.2" fill="none" stroke="#b9b9b9" stroke-width="1.4"/><path d="M6.3 6.3 9.5 9.5" stroke="#b9b9b9" stroke-width="1.6"/></svg>Property Inspections</li>
      <li class="nav-item"><svg viewBox="0 0 10 10"><rect x="0" y="9" width="10" height="1"/><rect x="1" y="5" width="1.5" height="4"/><rect x="4" y="2" width="1.5" height="7"/><rect x="7" y="4" width="1.5" height="5"/></svg>Energy Management</li>
      <li class="nav-item"><svg viewBox="0 0 10 10"><path d="M5 0 10 10H0Z"/></svg>Risk Management</li>
      <li class="nav-item"><svg viewBox="0 0 10 10"><rect x="0" y="1" width="10" height="2"/><rect x="0" y="4.5" width="10" height="2"/><rect x="0" y="8" width="10" height="2"/></svg>Project Management</li>
      <li class="nav-item"><svg viewBox="0 0 10 10"><rect x="0" y="2" width="10" height="6" fill="none" stroke="#b9b9b9" stroke-width="1.2"/><circle cx="5" cy="5" r="1.5"/></svg>Financial-Budgeting</li>
      <li class="nav-item"><svg viewBox="0 0 10 10"><ellipse cx="5" cy="4.5" rx="4.5" ry="3.5"/><path d="M2 7 1 10 5 7.5Z"/></svg>Tenant Requests</li>
      <li class="nav-item"><svg viewBox="0 0 10 10"><path d="M1.5 0H6.5L8.5 2V10H1.5Z"/></svg>Reports</li>
      <li class="nav-item"><svg viewBox="0 0 10 10"><path d="M0 9 3.5 5 6 7 10 2" fill="none" stroke="#b9b9b9" stroke-width="1.3"/></svg>Visual Reports</li>
      <li class="nav-item"><svg viewBox="0 0 10 10"><path d="M1.5 0H6.5L8.5 2V10H1.5Z"/></svg>Files</li>
      <li class="nav-item"><svg viewBox="0 0 10 10"><rect x="0" y="2" width="7" height="8"/><rect x="3" y="0" width="7" height="8" fill-opacity=".6"/></svg>Pages</li>
      <li class="nav-item"><svg viewBox="0 0 10 10"><circle cx="3.5" cy="6" r="3"/><circle cx="8" cy="2.5" r="2"/></svg>Configurations</li>
      <li class="nav-item"><svg viewBox="0 0 10 10"><path d="M9 1A2.5 2.5 0 0 0 6 4L0.5 8.5 1.5 9.5 6 4A2.5 2.5 0 0 0 9 1L7.5 2.5 7 3 7.5 1.5Z"/></svg>Settings</li>
    </ul>

    <section class="stat" style="left:187px">
      <svg viewBox="0 0 10 10"><path d="M5 0 10 5H8.5V10H6V7H4V10H1.5V5H0Z"/></svg>
      <div class="stat-value">3</div><div class="stat-label">Properties</div>
    </section>
    <section class="stat" style="left:327px">
      <svg viewBox="0 0 10 10"><circle cx="3" cy="3" r="2"/><circle cx="7" cy="3" r="2"/><rect x="0" y="6" width="10" height="4" rx="2"/></svg>
      <div class="stat-value">8</div><div class="stat-label">Tenants</div>
    </section>
    <section class="stat" style="left:466px">
      <svg viewBox="0 0 10 10"><path d="M0 0H4L2.8 1.2 4.5 2.9 2.9 4.5 1.2 2.8 0 4ZM10 0V4L8.8 2.8 7.1 4.5 5.5 2.9 7.2 1.2 6 0ZM0 10V6L1.2 7.2 2.9 5.5 4.5 7.1 2.8 8.8 4 10ZM10 10H6L7.2 8.8 5.5 7.1 7.1 5.5 8.8 7.2 10 6Z"/></svg>
      <div class="stat-value">422,000.00<small>Sq.Ft</small></div><div class="stat-label">Total Properties Area</div>
    </section>
    <section class="stat" style="left:606px">
      <svg viewBox="0 0 10 10"><path d="M0 0H4L2.8 1.2 4.5 2.9 2.9 4.5 1.2 2.8 0 4ZM10 0V4L8.8 2.8 7.1 4.5 5.5 2.9 7.2 1.2 6 0ZM0 10V6L1.2 7.2 2.9 5.5 4.5 7.1 2.8 8.8 4 10ZM10 10H6L7.2 8.8 5.5 7.1 7.1 5.5 8.8 7.2 10 6Z"/></svg>
      <div class="stat-value">233,500.00<small>Sq.Ft</small></div><div class="stat-label">Rented Area</div>
    </section>
    <section class="stat" style="left:745px">
      <svg viewBox="0 0 10 10"><path d="M0 0H4L2.8 1.2 4.5 2.9 2.9 4.5 1.2 2.8 0 4ZM10 0V4L8.8 2.8 7.1 4.5 5.5 2.9 7.2 1.2 6 0ZM0 10V6L1.2 7.2 2.9 5.5 4.5 7.1 2.8 8.8 4 10ZM10 10H6L7.2 8.8 5.5 7.1 7.1 5.5 8.8 7.2 10 6Z"/></svg>
      <div class="stat-value">188,500.00<small>Sq.Ft</small></div><div class="stat-label">Vacancies Area</div>
    </section>

    <nav class="range">
      <span class="on">&#9719; Last 7 days</span><span class="sep">|</span>&#9719; Last Months<span class="sep">|</span>&#9719; Last 3 Months<span class="sep">|</span>&#9719; Next 7 days<span class="sep">|</span>&#9719; Next Months<span class="sep">|</span>&#9719; Next 3 Months
    </nav>

    <section class="chart">
      <svg width="691" height="361" viewBox="0 0 691 361">
        <g fill="#0a8dff"><rect x="8" y="10" width="1.5" height="2"/><rect x="10.5" y="8" width="1.5" height="4"/><rect x="13" y="6" width="1.5" height="6"/><rect x="15.5" y="4" width="1.5" height="8"/></g>
        <text x="25" y="13" font-size="10" fill="#3a3a3a">12/27/2020 - 01/03/2021</text>

        <g stroke="#ececec" stroke-width="1">
          <line x1="26" y1="39" x2="686" y2="39"/><line x1="26" y1="68" x2="686" y2="68"/>
          <line x1="26" y1="97" x2="686" y2="97"/><line x1="26" y1="126" x2="686" y2="126"/>
          <line x1="26" y1="155" x2="686" y2="155"/>
        </g>
        <line x1="26" y1="184" x2="686" y2="184" stroke="#d5d5d5"/>
        <g stroke="#d5d5d5"><line x1="93" y1="184" x2="93" y2="189"/><line x1="180" y1="184" x2="180" y2="189"/><line x1="267" y1="184" x2="267" y2="189"/><line x1="353" y1="184" x2="353" y2="189"/><line x1="440" y1="184" x2="440" y2="189"/><line x1="527" y1="184" x2="527" y2="189"/><line x1="613" y1="184" x2="613" y2="189"/></g>

        <g font-size="7.5" fill="#8a8a8a">
          <text x="7" y="42">1.25</text><text x="7" y="71">1</text><text x="7" y="100">0.75</text>
          <text x="7" y="129">0.5</text><text x="7" y="158">0.25</text><text x="7" y="187">0</text>
        </g>
        <g font-size="7.5" fill="#8a8a8a" text-anchor="middle">
          <text x="47" y="202">12/27/2020</text><text x="133" y="202">12/28/2020</text><text x="221" y="202">12/29/2020</text>
          <text x="308" y="202">12/30/2020</text><text x="395" y="202">12/31/2020</text><text x="482" y="202">01/01/2021</text>
          <text x="569" y="202">01/02/2021</text><text x="689" y="202" text-anchor="end">01/03/2021</text>
        </g>

        <rect x="275" y="68" width="3" height="116" fill="#0a8dff"/>

        <g font-size="8" fill="#5a5a5a">
          <rect x="26" y="225" width="7" height="7" fill="#a9c8ea"/><text x="43" y="231">Scheduled Maintenance</text>
          <rect x="26" y="243" width="7" height="7" fill="#7ed66b"/><text x="43" y="249">Completed Scheduled Maintenance</text>
          <rect x="26" y="261" width="7" height="7" fill="#f59a4a"/><text x="43" y="267">Future Scheduled Maintenance</text>
          <rect x="26" y="279" width="7" height="7" fill="#3b3f4a"/><text x="43" y="285">Scheduled Work Orders</text>
          <rect x="26" y="297" width="7" height="7" fill="#7b80e0"/><text x="43" y="303">Completed Work Orders</text>
          <rect x="26" y="315" width="7" height="7" fill="#ee5a78"/><text x="43" y="321">Property Inspections in Progress</text>
          <rect x="26" y="333" width="7" height="7" fill="#e8d45a"/><text x="43" y="339">Completed Property Inspections</text>
        </g>

        <rect x="193" y="358" width="425" height="2" rx="1" fill="#dcdcdc"/>
      </svg>
    </section>

  </main>
</div>
</body>
</html>
```